Business card design and logo for plumbing bussiness

We are wanting a logo for a plumbing business is Queensland Australia. KLV Plumbing and Drainage will be doing works on domestic and commercial sites.
Plumbing, drainage and gas works. We are wanting something that will stand out and be noticed. Colours could be black blue and white but open for suggestions.

Target Market(s)

Builders and home renovators

Industry/Entity Type

Plumbing

Contact Information for Business Card

Dorian Machell - Director
0417 582 031
dorian@klvplumbing-example.com.au
QBCC: 374 8106
ABN: 52 913 207 615

Font styles to use
Sans Serif

Colors
000000

Requirements
Must have
• Clear defined branding

```html
<!DOCTYPE html>
<html lang="en">
<head>
<meta charset="utf-8">
<title>KLV Plumbing and Drainage – Business Card</title>
<link rel="stylesheet" href="https://fonts.googleapis.com/css2?family=Titillium+Web:wght@300;400;600;700&display=swap">
<style>
  :root {
    --backdrop: #2b2b2b;
    --card-dark: #222222;
    --card-light: #f4f4f4;
    --ink-dark: #3a3a3a;
    --ink-grey: #b9b9b9;
    --ink-tag-dark: #a8a8a8;
    --accent-blue: #3aa6e0;
    --accent-orange: #f0922b;
  }
  * { box-sizing: border-box; margin: 0; padding: 0; }
  html, body {
    width: 1200px;
    height: 716px;
    overflow: hidden;
    background: var(--backdrop);
    font-family: "Titillium Web", sans-serif;
  }
  .canvas {
    position: relative;
    width: 1200px;
    height: 716px;
  }
  .card {
    position: absolute;
    width: 530px;
    height: 300px;
    border-radius: 18px;
    overflow: hidden;
    box-shadow: 0 14px 30px rgba(0,0,0,0.45);
  }
  .card-front {
    left: 60px;
    top: 50px;
    background: var(--card-dark);
  }
  .card-back {
    left: 620px;
    top: 300px;
    background: var(--card-light);
  }
  .brand {
    position: absolute;
    text-align: center;
  }
  .brand-name {
    display: flex;
    align-items: center;
    justify-content: center;
    gap: 10px;
    font-weight: 600;
    line-height: 1;
    letter-spacing: 2px;
  }
  .brand-dot {
    border-radius: 50%;
    background: var(--accent-blue);
  }
  .brand-tagline {
    font-weight: 400;
    text-transform: uppercase;
    white-space: nowrap;
  }
  .card-front .brand {
    left: 0; right: 0; top: 96px;
  }
  .card-front .brand-name { font-size: 70px; color: var(--ink-grey); }
  .card-front .brand-dot { width: 12px; height: 12px; }
  .card-front .brand-tagline { font-size: 19px; color: var(--ink-tag-dark); margin-top: 6px; }

  .card-back .brand {
    left: 24px; top: 70px; width: 236px;
  }
  .card-back .brand-name { font-size: 52px; color: var(--ink-dark); }
  .card-back .brand-dot { width: 9px; height: 9px; }
  .card-back .brand-tagline { font-size: 13.5px; color: var(--ink-dark); margin-top: 4px; }

  .contact {
    position: absolute;
    left: 280px;
    right: 18px;
    top: 72px;
    color: var(--ink-dark);
  }
  .contact-name { font-size: 22px; line-height: 1.1; }
  .contact-name .first { font-weight: 300; }
  .contact-name .last { font-weight: 700; }
  .contact-role { font-size: 15px; color: var(--accent-blue); margin-bottom: 6px; }
  .contact-line {
    display: flex;
    align-items: center;
    gap: 7px;
    font-size: 12.5px;
    line-height: 1.7;
    white-space: nowrap;
  }
  .contact-line svg { flex: none; }
  .registration {
    position: absolute;
    left: 30px;
    bottom: 36px;
    font-size: 15px;
    color: var(--accent-orange);
    letter-spacing: 0.5px;
  }
  .registration .divider { margin: 0 10px; }

  .logo-lockup {
    position: absolute;
    left: 50px;
    top: 560px;
    text-align: center;
  }
  .logo-lockup .brand-name { font-size: 72px; color: #cfcfcf; }
  .logo-lockup .brand-dot { width: 12px; height: 12px; }
  .logo-lockup .brand-tagline { font-size: 21px; color: #bdbdbd; margin-top: 4px; }
  .logo-lockup .brand { position: static; }
</style>
</head>
<body>
<main class="canvas">

  <section class="card card-front" aria-label="Card front">
    <div class="brand">
      <div class="brand-name"><span class="brand-dot"></span>KLV</div>
      <div class="brand-tagline">Plumbing, Drainage and Gas Works</div>
    </div>
  </section>

  <section class="card card-back" aria-label="Card back">
    <div class="brand">
      <div class="brand-name"><span class="brand-dot"></span>KLV</div>
      <div class="brand-tagline">Plumbing, Drainage and Gas Works</div>
    </div>

    <div class="contact">
      <div class="contact-name"><span class="first">Dorian</span> <span class="last">Machell</span></div>
      <div class="contact-role">Director</div>
      <div class="contact-line">
        <svg width="14" height="12" viewBox="0 0 14 12" aria-hidden="true">
          <path d="M1 4 Q7 -1 13 4 L11 5.5 L9.5 4 L4.5 4 L3 5.5 Z" fill="var(--accent-blue)"/>
          <rect x="3" y="6" width="8" height="5" rx="1" fill="var(--accent-blue)"/>
        </svg>
        <span>0417 582 031</span>
      </div>
      <div class="contact-line">
        <svg width="14" height="10" viewBox="0 0 14 10" aria-hidden="true">
          <rect x="0.5" y="0.5" width="13" height="9" fill="var(--accent-blue)"/>
          <path d="M0.5 0.5 L7 6 L13.5 0.5" fill="none" stroke="#fff" stroke-width="1"/>
        </svg>
        <span>dorian@klvplumbing-example.com.au</span>
      </div>
    </div>

    <div class="registration">QBCC: 374 8106<span class="divider">|</span>ABN: 52 913 207 615</div>
  </section>

  <section class="logo-lockup" aria-label="Logo lockup">
    <div class="brand">
      <div class="brand-name"><span class="brand-dot"></span>KLV</div>
      <div class="brand-tagline">Plumbing, Drainage and Gas Works</div>
    </div>
  </section>

</main>
</body>
</html>
```